Migration Lawyers

Company: Dunstan & Co Lawyers & Migration Agents

Name: Graham Dunstan BEc, LLB
Address: Level 18, 72 Hollis Street
Sydney, NSW, Australia 2000

Ph: +61 2 9384 5207
M: 0428316540
E: graham@permitpath-example.org.au
W: www.permitpath-example.org.au

Target Market(s)

Migration Clients

Industry/Entity Type

It Company

Font styles to use
Script

Requirements
Must have
• Logo
Should not have
• Please scale the format to the printing size attached

```html
<!DOCTYPE html>
<html lang="en">
<head>
<meta charset="utf-8">
<title>Dunstan &amp; Co — Business Card</title>
<link rel="stylesheet" href="https://fonts.googleapis.com/css2?family=Pinyon+Script&display=swap">
<style>
  :root {
    --page-bg: #d9d9d9;
    --card-black: #050505;
    --card-edge: #1a1a1a;
    --ink-silver: #e6e6e6;
    --ink-soft: #bdbdbd;
    --mark-ring: #3a3a3a;
    --ghost-ring: #1c1c1c;
  }
  * { box-sizing: border-box; margin: 0; padding: 0; }
  html, body {
    width: 1200px;
    height: 873px;
    overflow: hidden;
    background: var(--page-bg);
  }
  .canvas {
    width: 1200px;
    height: 873px;
    display: flex;
    flex-direction: column;
    align-items: center;
    justify-content: center;
    gap: 44px;
  }
  .card {
    position: relative;
    width: 660px;
    height: 377px;
    background: var(--card-black);
    border: 1px solid var(--card-edge);
    box-shadow: 0 10px 28px rgba(0, 0, 0, 0.28);
    color: var(--ink-silver);
    font-family: "Pinyon Script", cursive;
    overflow: hidden;
  }

  /* Front side */
  .card--front .brand {
    position: absolute;
    left: 150px;
    top: 96px;
    display: flex;
    align-items: center;
    gap: 26px;
  }
  .brand__mark {
    width: 108px;
    height: 108px;
    flex: none;
  }
  .brand__text { display: flex; flex-direction: column; }
  .brand__name {
    font-size: 58px;
    line-height: 1;
    color: var(--ink-silver);
  }
  .brand__tagline {
    font-size: 25px;
    line-height: 1.2;
    margin-top: 8px;
    color: var(--ink-silver);
  }
  .card--front .website {
    position: absolute;
    left: 0;
    right: 0;
    bottom: 82px;
    text-align: center;
    font-size: 24px;
    color: var(--ink-soft);
  }

  /* Back side */
  .card--back .ghost-mark {
    position: absolute;
    left: 300px;
    top: 120px;
    width: 190px;
    height: 190px;
  }
  .contact {
    position: absolute;
    left: 56px;
    top: 40px;
    list-style: none;
  }
  .contact__name {
    font-size: 40px;
    line-height: 1.1;
  }
  .contact__degree {
    font-size: 21px;
    color: var(--ink-soft);
    margin: 2px 0 18px 18px;
  }
  .contact__line {
    font-size: 25px;
    line-height: 1.38;
    color: var(--ink-silver);
  }
</style>
</head>
<body>
<main class="canvas">

  <section class="card card--front" aria-label="Business card front">
    <div class="brand">
      <svg class="brand__mark" viewBox="0 0 108 108" aria-hidden="true">
        <circle cx="54" cy="54" r="50" fill="none" stroke="var(--mark-ring)" stroke-width="3"/>
      </svg>
      <div class="brand__text">
        <h1 class="brand__name">Dunstan &amp; Co</h1>
        <p class="brand__tagline">Lawyers &amp; Migration Agents</p>
      </div>
    </div>
    <p class="website">www.permitpath-example.org.au</p>
  </section>

  <section class="card card--back" aria-label="Business card back">
    <svg class="ghost-mark" viewBox="0 0 190 190" aria-hidden="true">
      <circle cx="95" cy="95" r="90" fill="none" stroke="var(--ghost-ring)" stroke-width="4"/>
    </svg>
    <ul class="contact">
      <li class="contact__name">Graham Dunstan</li>
      <li class="contact__degree">BEc, LLB</li>
      <li class="contact__line">Level 18, 72 Hollis Street</li>
      <li class="contact__line">Australia, Sydney, NSW 2000</li>
      <li class="contact__line">Tel. +61 2 9384 5207</li>
      <li class="contact__line">Mob. 0428316540</li>
      <li class="contact__line">graham@permitpath-example.org.au</li>
    </ul>
  </section>

</main>
</body>
</html>
```